spanish seafood rice meal

Hi, I need a design for Spanish seafood rice meal. The aimed market is North America and European. Please use the picture of my product I uploaded, it can be the cover of packaging. Also I upload a sample I found from supermarket. Please use simple colour. The size is 220mm*155mm*40mm. Thanks.

```html
<!DOCTYPE html>
<html lang="en">
<head>
<meta charset="UTF-8">
<title>Spanish Seafood Rice Meal – Packaging</title>
<link href="https://fonts.googleapis.com/css2?family=Playball&display=swap" rel="stylesheet">
<style>
  :root {
    --page-bg: #eef1f3;
    --teal: #a8dcdf;
    --panel: #ececec;
    --panel-light: #f5f5f5;
    --ink: #262626;
    --gold: #e2b43a;
    --dish: #2b2b2d;
  }
  html, body {
    margin: 0;
    padding: 0;
    width: 1200px;
    height: 840px;
    overflow: hidden;
    background: var(--page-bg);
  }
  .canvas {
    position: relative;
    width: 1200px;
    height: 840px;
    display: flex;
    align-items: center;
    justify-content: center;
  }
  .package {
    display: flex;
    box-shadow: 0 10px 30px rgba(0,0,0,0.12);
  }
  /* Spine (40 mm) */
  .spine {
    position: relative;
    width: 136px;
    height: 748px;
    background: var(--teal);
    overflow: hidden;
  }
  .spine-panel {
    position: absolute;
    left: 0;
    right: 0;
    top: 92px;
    bottom: 78px;
    background: linear-gradient(90deg, #d9d9d9, var(--panel));
  }
  .spine-title {
    position: absolute;
    left: 50%;
    top: 50%;
    transform: translate(-50%, -50%) rotate(-90deg);
    white-space: nowrap;
    font-family: "Playball", cursive;
    font-size: 46px;
    line-height: 1.05;
    color: var(--ink);
    margin: 0;
  }
  .spine-title span { display: block; }
  .spine-title .line-two { padding-left: 120px; }

  /* Front (155 mm x 220 mm) */
  .front {
    position: relative;
    width: 527px;
    height: 748px;
    background: var(--teal);
    overflow: hidden;
  }
  .front-panel {
    position: absolute;
    left: 0;
    right: 0;
    top: 78px;
    bottom: 42px;
    background: var(--panel);
    clip-path: polygon(70px 0, 100% 0, 100% calc(100% - 70px), calc(100% - 70px) 100%, 0 100%, 0 70px);
  }
  .backdrop-photo {
    position: absolute;
    left: 40px;
    right: 0;
    top: 20px;
    height: 300px;
    border-radius: 0 0 0 60% / 0 0 0 40%;
    background: radial-gradient(ellipse at 55% 55%, #fbfbfa 0%, #f0efec 55%, #e6e6e6 100%);
  }
  .base-surface {
    position: absolute;
    left: 0;
    right: 0;
    bottom: 0;
    height: 160px;
    background: linear-gradient(180deg, var(--panel-light), #e3e3e3);
  }
  .hero-photo {
    position: absolute;
    left: 18px;
    right: 14px;
    top: 300px;
    height: 230px;
    border-radius: 50%;
    background: radial-gradient(ellipse at 50% 50%, #f1cf6a 0%, var(--gold) 55%, #c99a2c 72%, var(--dish) 78%, #1c1c1e 100%);
  }
  .product-title {
    position: absolute;
    left: 40px;
    top: 122px;
    margin: 0;
    font-family: "Playball", cursive;
    font-weight: 400;
    font-size: 52px;
    line-height: 1.1;
    color: var(--ink);
    width: 460px;
  }
  .product-title span { display: block; }
  .product-title .line-two { padding-left: 160px; }
</style>
</head>
<body>
  <main class="canvas">
    <div class="package">
      <section class="spine">
        <div class="spine-panel"></div>
        <p class="spine-title"><span>Spanish Seafood</span><span class="line-two">Rice Meal</span></p>
      </section>
      <section class="front">
        <div class="front-panel">
          <div class="base-surface"></div>
          <div class="backdrop-photo" role="img" aria-label="Faded photo of a bowl of seafood rice with mussels and squid"></div>
          <div class="hero-photo" role="img" aria-label="Photo of Spanish seafood rice with mussels, prawns, squid and scallops in a dark oval pan"></div>
        </div>
        <h1 class="product-title"><span>Spanish Seafood</span><span class="line-two">Rice Meal</span></h1>
      </section>
    </div>
  </main>
</body>
</html>
```